Fern Acupuncture Business Card Design

I would like a business card design for my acupuncture business which is based from 2 practices in Melbourne, Australia.

The front of the card should include:

*The Logo
* Name - Marnie Dobrowen (B.App.Sc.(TCM), Dip.Rem.Mass.). (I would like the letters after my name in slightly smaller font)
* Mobile number - 0491 570 313
* Web address - www.fernacupuncture-demo.com.au

On the back of the card I would somehow like to fit my 2 clinic addresses in. They are:

The Quiet Grove & Renewal Studio
842 Brindle St, Camberwell VIC 3124
Ph: 1300 482 177

Wattle Lane Integrative & Restorative Care Clinic
19 Ostler Rd, Malvern East VIC 3145
Ph: (03) 9018 4472

If there is space, I'd also like to add to the back of the card - Next Appointment............................ (or something along those lines).

Thanks and happy designing!

Target Market(s)

Health consumers, and colleagues in the health industry

Industry/Entity Type

Clinic

Contact Information for Business Card

as above in brief

Requirements
Must have
• I've seen some ok designs coming in, however I'd like to avoid the generic look with the added curved line details etc. I don't particularly need extra patterns added to the card. I'd prefer it to look quite clean and simple, and using more earthy colours (I'm not super keen on the lime green that a lot of designs seem to include. I don't mind the full black or white look, (obviously the back side needs to be a lighter colour to allow me to write appointment details on it). I also quite like the idea of the background looking like brown recycled paper (just an idea - that's not 100% necessary).
Nice to have
• I have an idea that I could have the main flower part of the logo printed as metallic.
Should not have
• Generic patterns and too much added detail.

```html
<!DOCTYPE html>
<html lang="en">
<head>
<meta charset="utf-8">
<title>Fern Acupuncture – Business Card</title>
<link rel="stylesheet" href="https://fonts.googleapis.com/css2?family=Open+Sans:wght@400;600;700&display=swap">
<style>
  :root {
    --page: #e9e6e1;
    --card-black: #141312;
    --ink-light: #efeae2;
    --ink-muted: #c9bfae;
    --gold: #c2a565;
    --gold-light: #dcc894;
    --kraft: #b8966b;
    --kraft-dark: #a78559;
    --earth-brown: #4a3523;
    --sage: #5d6b3f;
    --ink-dark: #231a12;
    --paper: #fbf8f2;
    --dots: #6b5a48;
  }
  * { box-sizing: border-box; margin: 0; padding: 0; }
  html, body { width: 1200px; height: 913px; overflow: hidden; }
  body {
    background: var(--page);
    font-family: "Open Sans", Arial, sans-serif;
    display: flex; flex-direction: column; align-items: center; justify-content: center;
    gap: 40px;
  }
  .card {
    position: relative; width: 700px; height: 400px; overflow: hidden;
    box-shadow: 0 6px 18px rgba(0,0,0,.18);
  }

  /* Front */
  .card-front { background: var(--card-black); color: var(--ink-light); }
  .card-front::after {
    content: ""; position: absolute; left: 0; right: 0; bottom: 0; height: 10px;
    background: linear-gradient(90deg, var(--gold), var(--gold-light), var(--gold));
  }
  .contact-list { position: absolute; top: 36px; right: 30px; list-style: none; text-align: right; }
  .contact-list li {
    display: flex; align-items: center; justify-content: flex-end; gap: 10px;
    font-size: 14px; line-height: 25px; color: var(--ink-muted);
  }
  .contact-icon { width: 14px; height: 14px; flex: none; }
  .brand { position: absolute; left: 62px; top: 172px; display: flex; align-items: center; gap: 16px; }
  .brand-dot { width: 42px; height: 42px; border-radius: 50%; background: var(--gold); }
  .brand-name { font-size: 28px; font-weight: 400; color: var(--ink-light); letter-spacing: .5px; }
  .practitioner { position: absolute; right: 30px; top: 290px; text-align: right; }
  .practitioner-name { font-size: 22px; font-weight: 700; color: var(--gold-light); }
  .practitioner-credentials { font-size: 13px; font-weight: 600; margin-top: 2px; color: var(--ink-muted); }

  /* Back */
  .card-back {
    background: linear-gradient(135deg, var(--kraft) 0%, var(--kraft-dark) 100%);
    color: var(--ink-dark);
  }
  .clinics { position: absolute; left: 38px; top: 30px; right: 30px; }
  .clinics-title { font-size: 15px; font-weight: 700; color: var(--earth-brown); letter-spacing: .5px; margin-bottom: 6px; }
  .clinic { margin-bottom: 4px; }
  .clinic-name { font-size: 15px; font-weight: 700; color: var(--sage); }
  .clinic-name::before { content: "»"; color: var(--earth-brown); margin-right: 10px; }
  .clinic-address { font-size: 14px; padding-left: 20px; line-height: 20px; }
  .appointment-box {
    position: absolute; left: 140px; top: 175px; width: 530px; height: 195px;
    background: var(--paper); color: var(--ink-dark);
    padding: 34px 28px 0; font-size: 16px; font-weight: 600;
  }
  .write-line { display: flex; align-items: flex-end; height: 46px; }
  .write-line .fill { flex: 1; border-bottom: 2px dotted var(--dots); margin-left: 6px; margin-bottom: 5px; }
</style>
</head>
<body>

<section class="card card-front" aria-label="Business card front">
  <ul class="contact-list">
    <li>0491 570 313
      <svg class="contact-icon" viewBox="0 0 14 14"><rect x="4" y="1" width="6" height="12" rx="1.5" fill="var(--gold)"/></svg></li>
    <li>marnie@fernacupuncture-demo.com.au
      <svg class="contact-icon" viewBox="0 0 14 14"><rect x="1" y="3" width="12" height="8" fill="var(--gold)"/><path d="M1,3 L7,8 L13,3" fill="none" stroke="var(--card-black)" stroke-width="1"/></svg></li>
    <li>www.fernacupuncture-demo.com.au
      <svg class="contact-icon" viewBox="0 0 14 14"><circle cx="7" cy="7" r="6" fill="var(--gold)"/></svg></li>
  </ul>

  <div class="brand">
    <span class="brand-dot"></span>
    <span class="brand-name">Fern Acupuncture</span>
  </div>

  <div class="practitioner">
    <p class="practitioner-name">Marnie Dobrowen</p>
    <p class="practitioner-credentials">B.App.Sc.(TCM), Dip.Rem.Mass.</p>
  </div>
</section>

<section class="card card-back" aria-label="Business card back">
  <div class="clinics">
    <h2 class="clinics-title">CLINIC ADDRESSES</h2>
    <div class="clinic">
      <p class="clinic-name">The Quiet Grove &amp; Renewal Studio</p>
      <p class="clinic-address">842 Brindle St, Camberwell VIC 3124 &nbsp;•&nbsp; Ph: 1300 482 177</p>
    </div>
    <div class="clinic">
      <p class="clinic-name">Wattle Lane Integrative &amp; Restorative Care Clinic</p>
      <p class="clinic-address">19 Ostler Rd, Malvern East VIC 3145 &nbsp;•&nbsp; Ph: (03) 9018 4472</p>
    </div>
  </div>

  <div class="appointment-box">
    <div class="write-line">Next Appointment <span class="fill"></span></div>
    <div class="write-line"><span class="fill"></span></div>
    <div class="write-line"><span class="fill"></span></div>
  </div>
</section>

</body>
</html>
```